Grace-Rooted Harvest Church OL- Theme for 2022

We, Grace-Rooted Harvest Church of Oak Landing, need a design for a 4' x 6' banner that will be placed on two walls in the main sanctuary. The banner is to communicate/advertise the church's theme for 2022, "He Will Make All Things New: A New You - 2022" Revelations 21:5. The design should include our logo and church name. Use the color purple. We have not worshipped in our church building since 2020 due to the COVID pandemic. This banner should be reflective of change, newness as we plan to re-enter the building this spring. Our congregation demographic is 95% African American, 5% Hispanic. Our home base is Tampa, Florida (USA), but we have a large social media following, primarily due to the pandemic.

Target Market(s)

Church members, Ages 1-99; male and female

Industry/Entity Type

Religious

Font styles to use
Serif

Colors
0094D4
00A9DD
6FCCEA
C7EBF8
E9F6FB
00AB8E
00BBA5
67D7C9
C6EFE9
E9F9F6
6B429C
8869AF
B7A5CE
E3DAEB
F3F0F8

Requirements
Must have
• Theme, scripture, church logo and color purple

```html
<!DOCTYPE html>
<html lang="en">
<head>
<meta charset="utf-8">
<title>He Will Make All Things New – Theme Banner 2022</title>
<link rel="stylesheet" href="https://fonts.googleapis.com/css2?family=Poppins:wght@800&family=Libre+Baskerville&family=Archivo:wght@400;700&display=swap">
<style>
  :root {
    --violet-deep: #453a98;
    --violet-mid: #6a379c;
    --magenta: #a83aa6;
    --magenta-bright: #c23fb0;
    --indigo-band: #4b2f8a;
    --plum: #7b3499;
    --gold-light: #ffe3a0;
    --gold: #e0a040;
    --umber: #3a2514;
    --white: #ffffff;
  }
  html, body {
    margin: 0;
    padding: 0;
    width: 1200px;
    height: 608px;
    overflow: hidden;
    background: #ffffff;
  }
  .banner {
    position: relative;
    width: 1200px;
    height: 608px;
    overflow: hidden;
  }
  .banner__shapes {
    position: absolute;
    inset: 0;
    width: 1200px;
    height: 608px;
  }
  .theme {
    position: absolute;
    left: 40px;
    top: 152px;
    width: 580px;
    margin: 0;
    color: var(--white);
    font-family: "Poppins", sans-serif;
    font-weight: 800;
    text-align: center;
    letter-spacing: -1.5px;
  }
  .theme__line {
    display: block;
    font-size: 61px;
    line-height: 68px;
  }
  .theme__line--year {
    margin-top: 18px;
    font-size: 64px;
  }
  .scripture {
    position: absolute;
    right: 623px;
    top: 392px;
    margin: 0;
    color: var(--white);
    font-family: "Libre Baskerville", serif;
    font-size: 25px;
  }
  .social {
    position: absolute;
    left: 78px;
    top: 516px;
    display: flex;
    align-items: center;
    gap: 10px;
    color: var(--white);
    font-family: "Archivo", sans-serif;
    font-size: 17px;
  }
  .social__dot {
    width: 24px;
    height: 24px;
    border-radius: 50%;
    background: var(--white);
  }
  .website {
    position: absolute;
    left: 78px;
    top: 548px;
    margin: 0;
    color: var(--white);
    font-family: "Archivo", sans-serif;
    font-size: 22px;
  }
  .church {
    position: absolute;
    left: 892px;
    top: 516px;
    margin: 0;
    color: var(--white);
    font-family: "Archivo", sans-serif;
    font-style: normal;
    line-height: 17.5px;
  }
  .church__name {
    display: block;
    font-weight: 700;
    font-size: 14px;
  }
  .church__address {
    display: block;
    font-size: 13.5px;
  }
</style>
</head>
<body>
<main class="banner">
  <svg class="banner__shapes" viewBox="0 0 1200 608" xmlns="http://www.w3.org/2000/svg">
    <defs>
      <linearGradient id="bg-gradient" x1="0" y1="0" x2="1" y2="0.3">
        <stop offset="0" stop-color="var(--violet-deep)"/>
        <stop offset="0.55" stop-color="var(--violet-mid)"/>
        <stop offset="1" stop-color="var(--magenta)"/>
      </linearGradient>
      <linearGradient id="lower-left-gradient" x1="0" y1="0" x2="1" y2="0">
        <stop offset="0" stop-color="var(--magenta)"/>
        <stop offset="0.5" stop-color="var(--plum)"/>
        <stop offset="1" stop-color="var(--indigo-band)"/>
      </linearGradient>
      <linearGradient id="lower-right-gradient" x1="0" y1="1" x2="1" y2="0">
        <stop offset="0" stop-color="var(--magenta-bright)"/>
        <stop offset="1" stop-color="var(--plum)"/>
      </linearGradient>
      <linearGradient id="edge-gradient" x1="0" y1="0" x2="0" y2="1">
        <stop offset="0" stop-color="var(--magenta-bright)"/>
        <stop offset="1" stop-color="var(--indigo-band)"/>
      </linearGradient>
      <radialGradient id="photo-gradient" cx="0.74" cy="0.3" r="0.75">
        <stop offset="0" stop-color="var(--gold-light)"/>
        <stop offset="0.3" stop-color="var(--gold)"/>
        <stop offset="0.75" stop-color="#7a4a1c"/>
        <stop offset="1" stop-color="var(--umber)"/>
      </radialGradient>
    </defs>

    <rect class="shape-background" width="1200" height="608" fill="url(#bg-gradient)"/>
    <polygon class="shape-photo-edge" points="522,0 550,0 750,472 740,608 712,608" fill="url(#edge-gradient)"/>
    <polygon class="shape-lower-left" points="0,400 750,600 750,608 0,608" fill="url(#lower-left-gradient)"/>
    <polygon class="shape-lower-left-band" points="0,408 520,560 750,608 430,608 0,470" fill="var(--indigo-band)" opacity="0.55"/>
    <polygon class="shape-lower-right" points="750,472 1200,258 1200,608 750,608" fill="url(#lower-right-gradient)"/>
    <polygon class="shape-lower-right-band" points="750,472 1200,258 1200,280 760,600" fill="var(--indigo-band)" opacity="0.7"/>

    <polygon class="photo-area" role="img"
      aria-label="Photograph: a person with arms outstretched in a sunlit stone archway, golden sunlight streaming over a cobbled path"
      points="522,0 1200,0 1200,258 750,472"
      fill="url(#photo-gradient)"/>
  </svg>

  <h1 class="theme">
    <span class="theme__line">He Will Make</span>
    <span class="theme__line">All Things New</span>
    <span class="theme__line theme__line--year">A New You - 2022</span>
  </h1>
  <p class="scripture">Revelations 21:5</p>

  <div class="social">
    <span class="social__dot"></span>
    <span class="social__handle">@grhcol</span>
  </div>
  <p class="website">www.grhcol.org</p>

  <address class="church">
    <span class="church__name">Grace-Rooted Harvest Church of</span>
    <span class="church__name">Oak Landing</span>
    <span class="church__address">4520 W. Oakmere Avenue Tampa, FL 33614</span>
  </address>
</main>
</body>
</html>
```